Flyer Design for Singapore's Leading Education Centre

We need a flyer design for our Education centre, Marcus Tavi Study Den, which is based in Singapore. Our classes are often very lively and engaging and our students genuinely looks forward to every lesson. Therefore our flyer should also emit such a feel - lively and engaging yet at the same time looking elegant and professional.

The flyer is to be designed on an A5 paper, double sided and portrait format.

You may refer to our website to have a better understanding of our company and its business. http://www.mtstudyden.com.sg/

The purpose of this flyer is to create awareness for our company, and of course, to increase sales. Nearly every household in Singapore receives a huge chunk of flyers in their letterbox daily. As such, our flyer must stand out from the crowd.

A sample flyer has been attached below. We are looking for something even more creative and outstanding.

Here are more details of the flyer:

On the front cover:

1) Logo
2) Company Name : Marcus Tavi Study Den
3) Important Information : Registered with the NBA (S/N 8katiyor)
4) Tel : 6382 9046
5) Email Us: enquiry@mtstudyden.com.sg
6) Address : BLK 418 Pasir Vale Road 2, #03-17, Singapore 140418

7) Heading/attention grabber : "More than 15 years of excellent teaching, we know what success is!" - Designer may feel free to edit or rephrase sentence so long as it sounds impressive and adds on to the reputation of the company.

8) Our Programs : Primary Mathematics, Heuristic Problem Solving, Secondary Additional & Elementary Mathematics, IP Program leading 'A' Levels Exam (Math), JC H2 Math ('A' Levels), Primary Science, Secondary Physics & Chemistry

9) Our Publications
- "Singapore's Best Selling Math Assessment Book in 2008"
- "Written by our Founder, Mr Marcus Tavi"

On the back page:

1) Why Choose Us
- Brain Training : Critical thinking and number sense taught in every lesson
- Focus Group for students who need more time to learn
- Fun and Easy-To-Understand methods that will help students remember key concepts with ease
- Lively and Engaging Lessons : No One Will Be Bored!

2) Testimonials ("Excerpts from our HUGE testimonial database"

"Dear Teacher, here is an A* just for you and I can say that your efforts have paid off. Thank you for all your help and support. I will definitely continue to study under you"
- Lim Wei Jun, Rosewater Primary School, Year 2013 (From C in P6 to A* in PSLE)

"Dear Mr Tavi, you are really an awesome math teacher. You make math lessons so fun and interesting! My math grade has really improved thanks to you. I am so grateful to have a teacher like you!"
- Mona Ke, Oakfield Bay Primary School, Year 2010. (A* for PSLE Math. Currently in Lantern Hill Girls'School)

"I scored an A2 for my Math! Thank you for your guidance during this short period of time in your classes. I remember getting F9s for all my Math tests until I know you. It has been an honor to be taught by you. They say its hard to be a teacher, and harder to get a good teacher. But looks like you are both!"
- Warren Lau, Pine Crest Secondary School, Year 2011 (From F9 in S4 to A2)

3) Visit our website to find out more about our programs!
http://www.mtstudyden.com.sg/

Dear designers, we have uploaded more photos of lessons. Do feel free to view them and see whichever photo is appropriate to be used for the flyer. 

Dear designers, our company will be hiring the same designer (the one who wins the current flyer project) for our next project (brochure). Submit your designs today!

Dear Designers, 

 

We have made somechanges to the contents that we want at the back of the flyer : 

 

*The third testimonialnow has a photograph to be inserted into as well. Please refer to the filesuploaded.

 

2) Testimonials("Excerpts from our HUGE testimonial database"

"Dear Teacher, here is an A* just for youand I can say that your efforts have paid off. Thank you for all your help andsupport. I will definitely continue to study under you" 
- Lim Wei Jun, Rosewater Primary School, Year 2013(From C in P6 to A* in PSLE)

"Dear Mr Tavi, you are really an awesomemath teacher. You make math lessons so fun and interesting! My math grade hasreally improved thanks to you. I am so grateful to have a teacher like you!"
- Mona Ke, Oakfield Bay Primary School, Year 2010.(A* for PSLE Math. Currently in Lantern Hill Girls'School) 

""Dear Teacher, Happy BelatedTeachers' Day! I really want to thank you for your guidance in math and life ingeneral. You've really changed me a lot. You taught me to love learning andthat nothing is hard if we're willing to try! I really enjoy your math lessons.And you're a truly dedicated teacher and mentor. I'm definitely going to workhard and make you proud! :) 

- Tan Hui Mei, BKJC, Year 2013 

Reason: We are extending the deadline to receive more designs.

Target Market(s)

Parents of age 30 - 50
Students of age 12 - 18

Industry/Entity Type

Teacher

Font styles to use
Serif
Sans Serif

Colors
0255a3
f37022
ffffff

Requirements
Must have
• 1) Important Information : Registered with the NBA (S/N 8katiyor)
2) Website: http://www.mtstudyden.com.sg/
Nice to have
• Photos of classes are provided in the zip/rar folders attached. Designer can use these photos as and when he/she deem fit.

```html
<!DOCTYPE html>
<html lang="en">
<head>
<meta charset="utf-8">
<title>Marcus Tavi Study Den – Flyer</title>
<link rel="stylesheet" href="https://fonts.googleapis.com/css2?family=Arimo:wght@400;700&family=Roboto+Condensed:wght@400;700;900&display=swap">
<style>
  :root {
    --blue: #0255a3;
    --blue-deep: #0a4794;
    --orange: #f37022;
    --white: #ffffff;
    --ink: #333333;
    --grey: #555555;
    --green: #2e8b3a;
    --red: #c8323c;
    --footer: #2f2f2f;
    --stage: #e9e9e9;
  }
  * { box-sizing: border-box; margin: 0; padding: 0; }
  html, body { width: 1200px; height: 907px; overflow: hidden; }
  body { background: var(--stage); font-family: "Arimo", Arial, sans-serif; position: relative; }

  .page {
    position: absolute; background: var(--white); overflow: hidden;
    box-shadow: 0 2px 8px rgba(0,0,0,.18);
  }
  .page--front { left: 62px; top: 108px; width: 526px; height: 735px; }
  .page--back  { left: 638px; top: 118px; width: 527px; height: 740px; }
  .abs { position: absolute; }

  .swoosh { position: absolute; left: 0; top: 0; }

  .brand { position: absolute; display: flex; align-items: center; gap: 6px; z-index: 2; }
  .brand__dot { width: 26px; height: 26px; border-radius: 50%; background: var(--blue); flex: none; }
  .brand__name { font-family: "Arimo", Arial, sans-serif; font-weight: 700; font-size: 10px; line-height: 12px; color: var(--blue); width: 76px; }

  .headline { font-family: "Roboto Condensed", "Arial Narrow", sans-serif; font-weight: 900; text-transform: uppercase; }
  .front-title { right: 20px; top: 36px; text-align: right; font-size: 29px; line-height: 34px; color: var(--blue); }
  .front-title .accent { color: var(--orange); }

  .photo { position: absolute; }
  .photo--group { left: 0; top: 105px; width: 526px; height: 225px;
    background: linear-gradient(180deg, #c9b5a3 0%, #8b8fa8 45%, #d8d8dc 85%, #ffffff 100%); }

  .success { left: 0; width: 526px; top: 338px; text-align: center; font-size: 33px; line-height: 38px; color: var(--ink); letter-spacing: .3px; }

  .label { position: absolute; height: 20px; color: var(--white); font-family: "Roboto Condensed", "Arial Narrow", sans-serif; font-weight: 700; font-size: 12.5px; line-height: 20px; text-align: center; text-transform: uppercase; }
  .label--blue { background: var(--blue); }
  .label--orange { background: var(--orange); }

  .book { position: absolute; border-radius: 2px; background: linear-gradient(160deg, #7a3aa0, #d8343c 60%, #f0a030); box-shadow: 2px 2px 4px rgba(0,0,0,.25); }

  .programs { left: 96px; width: 334px; top: 420px; text-align: center; white-space: nowrap;
    font-family: "Roboto Condensed", "Arial Narrow", sans-serif; font-weight: 400;
    font-size: 11px; line-height: 15px; color: var(--grey); text-transform: uppercase; }
  .publication { left: 63px; width: 400px; top: 543px; text-align: center; white-space: nowrap;
    font-family: "Roboto Condensed", "Arial Narrow", sans-serif; font-weight: 400;
    font-size: 11.5px; line-height: 14.5px; color: var(--ink); text-transform: uppercase; }

  .rule { position: absolute; left: 0; width: 100%; height: 3px; }
  .rule--green { background: var(--green); }
  .rule--blue { background: var(--blue); }

  .corner { position: absolute; border-radius: 50%; border: 7px solid var(--orange); }
  .corner--left { left: -120px; top: 560px; width: 240px; height: 240px; background: linear-gradient(135deg, #e5e5e5, #b9b3ad); }
  .corner--right { left: 418px; top: 555px; width: 240px; height: 240px; background: linear-gradient(135deg, #e4ddd6, #a9a6a3); }

  .phone { left: 0; width: 526px; top: 612px; display: flex; justify-content: center; align-items: center; gap: 8px; }
  .phone__num { font-family: "Roboto Condensed", "Arial Narrow", sans-serif; font-weight: 700; font-size: 32px; color: var(--red); }

  .web { position: absolute; background: var(--blue-deep); color: var(--white); text-align: center; border: 2px solid #6f8fc0; }
  .web--front { left: 106px; top: 655px; width: 280px; height: 40px; font-size: 21px; line-height: 36px; }
  .web--back { left: 140px; top: 668px; width: 242px; height: 30px; font-size: 17px; line-height: 26px; }

  .footer { position: absolute; left: 0; width: 100%; height: 23px; background: var(--footer); color: var(--white); text-align: center; font-size: 13.5px; line-height: 23px; text-transform: uppercase; }
  .page--front .footer { top: 712px; }
  .page--back .footer { top: 717px; }

  .why { left: 22px; width: 392px; top: 70px; font-size: 11.5px; line-height: 15.5px; color: var(--grey); }
  .testimonials { left: 22px; width: 398px; top: 186px; font-size: 10.8px; line-height: 14.5px; color: var(--grey); }
  .testimonials p { margin-bottom: 14px; }

  .photo--circle { left: 398px; top: 388px; width: 250px; height: 250px; border-radius: 50%; border: 7px solid var(--blue);
    background: linear-gradient(135deg, #d7d6d2, #8e959c); }
  .enable { left: 22px; top: 448px; font-size: 30px; line-height: 32px; color: var(--orange); }
  .enable .blue { color: var(--blue); }

  .photo--class { left: 0; top: 526px; width: 527px; height: 125px;
    background: linear-gradient(180deg, #ececec 0%, #b9c2cf 50%, #7e90b4 100%); }
</style>
</head>
<body>

<section class="page page--front" aria-label="Flyer front">
  <svg class="swoosh" width="526" height="110" viewBox="0 0 526 110" aria-hidden="true">
    <path d="M0 90 C120 20 300 0 526 8 L526 0 L0 0 Z" fill="#f4f4f4"/>
    <path d="M0 92 C140 30 300 10 526 12 L526 4 C300 2 130 22 0 84 Z" fill="var(--orange)"/>
    <path d="M250 8 C360 2 450 2 526 4 L526 0 L260 0 Z" fill="var(--blue)"/>
  </svg>
  <div class="brand" style="left:14px;top:28px;">
    <span class="brand__dot"></span>
    <span class="brand__name">Marcus Tavi Study Den</span>
  </div>
  <h1 class="abs headline front-title"><span class="accent">15 Years</span> of Excellent<br>Teaching</h1>

  <div class="photo photo--group" role="img" aria-label="Photo of the teacher standing with a smiling group of students"></div>

  <h2 class="abs headline success">We Know What Success Is</h2>

  <div class="label label--blue" style="left:170px;top:385px;width:182px;">Our Programs :</div>
  <div class="book" style="left:8px;top:405px;width:80px;height:60px;" role="img" aria-label="Maths assessment book cover"></div>
  <div class="book" style="left:14px;top:440px;width:78px;height:92px;" role="img" aria-label="Maths assessment book cover"></div>
  <div class="book" style="left:432px;top:410px;width:72px;height:122px;" role="img" aria-label="Maths assessment book cover"></div>

  <p class="abs programs">Primary Mathematics, Heuristic Problem Solving,<br>Secondary Additional &amp; Elementary Mathematics, IP Program<br>leading 'A'Levels Exam (Math), JC H2 Math ('A' Levels), Primary<br>Science, Secondary Physics &amp; Chemistry</p>

  <div class="rule rule--green" style="top:497px;"></div>
  <div class="rule rule--blue" style="top:501px;"></div>

  <div class="label label--orange" style="left:170px;top:512px;width:180px;">Our Publication :</div>
  <p class="abs publication">Our Publications<br>Singapore's Best Selling Mathematics Assessment Book in 2008"<br>More than 400,000 copies sold! ... and counting!"<br>Written by our founder, Mr Marcus Tavi"</p>

  <div class="corner corner--left" role="img" aria-label="Photo of a teacher writing on a whiteboard"></div>
  <div class="corner corner--right" role="img" aria-label="Photo of a student working at a desk"></div>

  <div class="abs phone">
    <svg width="26" height="26" viewBox="0 0 26 26" aria-hidden="true">
      <circle cx="13" cy="13" r="12" fill="none" stroke="#222" stroke-width="2"/>
      <path d="M8 7 L11 7 L12 10 L10.5 11.5 C11.5 13.5 12.5 14.5 14.5 15.5 L16 14 L19 15 L19 18 C13 19 7 13 8 7 Z" fill="#222"/>
    </svg>
    <span class="phone__num">6382 9046</span>
  </div>

  <div class="web web--front">www.mtstudyden.com.sg</div>
  <div class="footer">BLK 418 Pasir Vale Road 2, #03-17, Singapore 140418</div>
</section>

<section class="page page--back" aria-label="Flyer back">
  <svg class="swoosh" width="527" height="100" viewBox="0 0 527 100" aria-hidden="true">
    <rect x="0" y="0" width="527" height="10" fill="var(--blue)"/>
    <path d="M0 10 L300 10 C400 14 480 40 527 90 L527 70 C470 30 400 16 300 14 L0 14 Z" fill="var(--orange)"/>
  </svg>
  <div class="brand" style="left:422px;top:24px;">
    <span class="brand__dot"></span>
    <span class="brand__name">Marcus Tavi Study Den</span>
  </div>

  <div class="label label--orange" style="left:17px;top:42px;width:133px;text-align:left;padding-left:8px;">Why Choose Us:</div>
  <p class="abs why">Brain Training : Critical thinking and number sense taught in every lesson Focus Group for students who need more time to learn Fun and Easy-To-Understand methods that will help students remember key concepts with ease Lively and Engaging Lessons : No One Will Be Bored!</p>

  <div class="label label--orange" style="left:17px;top:152px;width:133px;text-align:left;padding-left:8px;">Testimonials:</div>
  <div class="abs testimonials">
    <p>Dear Teacher, here is an A* just for you and I can say that your efforts have paid off. Thank you for all your help and support. I will definitely continue to study under you" Lim Wei Jun, Rosewater Primary School, Year 2013 (From C in P6 to A* in PSLE)</p>
    <p>Dear Mr Tavi, you are really an awesome math teacher. You make math lessons so fun and interesting! My math grade has really improved thanks to you. I am so grateful to have a teacher like you!" Mona Ke, Oakfield Bay Primary School, Year 2010. (A* for PSLE Math. Currently in Lantern Hill Girls'School)</p>
    <p>I scored an A2 for my Math! Thank you for your guidance during this short period of time in your classes. I remember getting F9s for all my Math tests until I know you. It has been an honor to be taught by you. They say its hard to be a teacher, and harder to get a good teacher. But looks like you are both!" Warren Lau, Pine Crest Secondary School, Year 2011 (From F9 in S4 to A2)</p>
  </div>

  <div class="book" style="left:446px;top:168px;width:74px;height:68px;" role="img" aria-label="Maths assessment book cover"></div>
  <div class="book" style="left:432px;top:215px;width:70px;height:70px;" role="img" aria-label="Maths assessment book cover"></div>
  <div class="book" style="left:440px;top:268px;width:76px;height:92px;" role="img" aria-label="Maths assessment book cover"></div>

  <div class="photo photo--circle" role="img" aria-label="Photo of a student in a classroom"></div>

  <h2 class="abs headline enable">Enable your child to<br><span class="blue">Score A's in school!</span></h2>

  <div class="rule rule--green" style="top:519px;"></div>
  <div class="photo photo--class" role="img" aria-label="Photo of the teacher with a group of young students in front of a whiteboard"></div>
  <div class="rule rule--green" style="top:651px;"></div>

  <div class="web web--back">www.mtstudyden.com.sg</div>
  <div class="footer">BLK 418 Pasir Vale Road 2, #03-17, Singapore 140418</div>
</section>

</body>
</html>
```